Card for Maori themed strategy game

Visual design of a type of card from a board game.
The card has a front and a back, back being a single large image, and with one of three small icons (in white) to represent which of the three periods of the game it is from, but otherwise there is no difference in the backs.
The front side carries most of the information, and hopefully an attractive design. Functionally, from top to bottom it has a title, a large text field, a type line, another text field, and some tracking information at the very bottom. Current layout with placeholder art is attached.
Note that the relative size of the two text boxes will vary from card to card.
The colour pallete is intended to be red black and white, for this particular design focusing primarily on red.

```html
<!DOCTYPE html>
<html lang="en">
<head>
<meta charset="utf-8">
<title>Card Designs – Māori Strategy Game</title>
<link rel="stylesheet" href="https://fonts.googleapis.com/css2?family=Nunito:ital,wght@0,400;0,600;0,700;0,800;1,700&display=swap">
<style>
  :root {
    --page: #ffffff;
    --card-red: #a8181c;
    --card-red-deep: #8e1216;
    --card-edge: #7a0f12;
    --frame-line: #d9705f;
    --panel: #3d1414;
    --panel-flavor: #451716;
    --panel-line: #ead2c8;
    --ink-light: #ffffff;
    --ink-soft: #f3e2dc;
    --mask-dark: #4a1512;
    --mask-mid: #b8402e;
  }
  * { box-sizing: border-box; margin: 0; padding: 0; }
  html, body { width: 1200px; height: 1000px; overflow: hidden; background: var(--page); }
  body { position: relative; font-family: "Nunito", sans-serif; }

  .card {
    position: absolute;
    width: 154px; height: 216px;
    background: radial-gradient(ellipse at 50% 40%, var(--card-red) 0%, var(--card-red-deep) 100%);
    border: 1px solid var(--card-edge);
    box-shadow: 0 1px 3px rgba(0,0,0,.35);
  }
  .card::before {
    content: ""; position: absolute; inset: 5px;
    border: 1px solid var(--frame-line);
    pointer-events: none;
  }

  /* Card back */
  .card-back .mask-art {
    position: absolute; left: 20px; top: 14px; width: 112px; height: 180px;
    border-radius: 48% 48% 44% 44% / 40% 40% 58% 58%;
    background: radial-gradient(ellipse at 50% 45%, var(--mask-mid) 0%, var(--mask-dark) 75%);
  }
  .card-back .period-badge {
    position: absolute; left: 58px; bottom: -1px; width: 38px; height: 26px;
    background: var(--panel);
    border-radius: 19px 19px 0 0;
    border: 1px solid var(--frame-line); border-bottom: none;
  }
  .card-back .period-icon {
    position: absolute; left: 11px; top: 7px; width: 16px; height: 12px;
    background: var(--ink-light); border-radius: 3px;
  }

  /* Card front */
  .card-front .layout {
    position: absolute; inset: 12px 11px 10px;
    display: flex; flex-direction: column; align-items: center;
  }
  .title-banner {
    width: 132px; height: 22px; flex: none;
    background: var(--panel);
    border: 1px solid var(--panel-line);
    border-radius: 66px 66px 6px 6px / 9px 9px 3px 3px;
    color: var(--ink-light);
    font-weight: 800; font-size: 9px; letter-spacing: .2px;
    text-transform: uppercase;
    display: flex; align-items: center; justify-content: center;
    padding-top: 2px;
  }
  .rules-box {
    width: 130px; flex: none; margin-top: 8px;
    background: var(--panel);
    border: 1px solid var(--panel-line);
    border-radius: 4px;
    color: var(--ink-light);
    font-weight: 700; font-size: 7.6px; line-height: 1.15;
    text-align: center;
    display: flex; flex-direction: column; justify-content: center;
    padding: 2px 5px;
  }
  .rules-box.compact { font-size: 6.4px; }
  .type-line {
    width: 58px; height: 13px; flex: none;
    background: var(--panel);
    border: 1px solid var(--ink-light);
    color: var(--ink-light);
    font-weight: 800; font-size: 7.5px;
    display: flex; align-items: center; justify-content: center;
  }
  .timing {
    flex: none; margin-top: 2px;
    color: var(--ink-soft);
    font-style: italic; font-weight: 700; font-size: 6px;
  }
  .flavor-box {
    width: 130px; flex: 1 1 auto;
    background: var(--panel-flavor);
    border-radius: 4px;
    color: var(--ink-light);
    font-size: 5px; line-height: 1.32; font-weight: 700;
    text-align: center;
    padding: 5px 6px;
    overflow: hidden;
  }
  .flavor-box.short { flex: none; }
</style>
</head>
<body>

<!-- Card backs: one per game period -->
<div class="card card-back" style="left:348px;top:46px;">
  <div class="mask-art" role="img" aria-label="Carved mask artwork"></div>
  <div class="period-badge"><div class="period-icon" role="img" aria-label="Period icon: canoe"></div></div>
</div>
<div class="card card-back" style="left:514px;top:46px;">
  <div class="mask-art" role="img" aria-label="Carved mask artwork"></div>
  <div class="period-badge"><div class="period-icon" role="img" aria-label="Period icon: crossed weapons"></div></div>
</div>
<div class="card card-back" style="left:684px;top:46px;">
  <div class="mask-art" role="img" aria-label="Carved mask artwork"></div>
  <div class="period-badge"><div class="period-icon" role="img" aria-label="Period icon: sailing ship"></div></div>
</div>

<!-- Row 1 fronts -->
<div class="card card-front" style="left:184px;top:278px;">
  <div class="layout">
    <div class="title-banner">Claiming the Land</div>
    <div class="rules-box" style="height:30px;">Place a Marae in the newly settled territory.</div>
    <div class="type-line" style="margin-top:5px;">Reaction</div>
    <div class="timing">Play when you settle a new territory</div>
    <div class="flavor-box" style="margin-top:3px;">Maori placed great value on their own whakapapa (heritage), and also wished to know the whakapapa of this new land. The arrivals made legends explaining how their gods and ancestors had shaped Aotearoa. This whakapapa helped them to understand their land, as well as giving them an ancestral claim to the territory. The people of Te Awa Roa say their ancestor Maunu went inland one day to repair his waka, but the day was long and the work hard, so he stopped often, carving out the great Waimaunu (water of Maunu) river.</div>
  </div>
</div>

<div class="card card-front" style="left:350px;top:278px;">
  <div class="layout">
    <div class="title-banner">Terrace Gardens</div>
    <div class="rules-box" style="height:30px;">Gain six food from your harvest of kumara</div>
    <div class="type-line" style="margin-top:5px;">Action</div>
    <div class="flavor-box" style="margin-top:9px;">With the moa extinct and the population growing, Maori turned to farming. Their key crop was kumara, a tropical plant which needed complex techniques to grow in the much colder Aotearoa. Gardens were dug in north facing hills (the warmest side), and laid with stones to further trap heat. The soil was mixed with gravel to make it drain well and had to be watched for birds and caterpillars that could damage the crop. Many of these gardens can be seen today, in the shape of reformed hills.</div>
  </div>
</div>

<div class="card card-front" style="left:518px;top:278px;">
  <div class="layout">
    <div class="title-banner">Influenza Epidemic</div>
    <div class="rules-box compact" style="height:50px;">Each other player is afflicted by the influenza in Pa to order. If they have five or more Rangatira, they downgrade two Rangatira to Ware. Otherwise, they downgrade one Rangatira to Ware</div>
    <div class="type-line" style="margin-top:5px;">Tribal</div>
    <div class="flavor-box" style="margin-top:5px;">Of all the new diseases Maori caught from their visitors, by far the most common. Infected patients cough constantly, the virus riding tiny particles of spit to a new host. Flu was not an especially lethal disease, but was the fastest to spread. Influenza is also notable for mutating quickly. A population would a year or two another strain would develop and cause its own epidemic.</div>
  </div>
</div>

<div class="card card-front" style="left:685px;top:278px;">
  <div class="layout">
    <div class="title-banner"></div>
    <div class="rules-box" style="height:26px;margin-top:6px;">Place a two neutral ware in a unoccupied coastal territory.</div>
    <div class="type-line" style="margin-top:6px;">Tribal</div>
    <div class="flavor-box" style="margin-top:9px;">Kahurangi was a noble child who died young, and upon his grave was planted a sapling. This tree grew great and strong, eventually being carved into the mighty waka Kahurangi. The great canoe set out for Aotearoa, captained by Tamarau. The waka made landfall near Whanga Iti before being carried by hand across the isthmus. It then sailed up and down the west coast, leaving hapu scattered across the central north island, a people to this day called the Kahurangi confederation.</div>
  </div>
</div>

<div class="card card-front" style="left:860px;top:283px;">
  <div class="layout">
    <div class="title-banner">Fortification</div>
    <div class="rules-box" style="height:54px;">Choose one of...<br>- Place a Pa in each of two nutral territories<br>- Upgrade one neutral Pa to a Great Pa</div>
    <div class="type-line" style="margin-top:6px;">Tribal</div>
    <div class="flavor-box" style="margin-top:6px;">Unlike Kainga and Marae which were built near resources, Pa were erected on defensible land like hills, peninsulas, lakes and gorge, where the hapu could shelter in times of conflict. A Pa was ringed with a palisade wall made of wooden stakes planted deep in the earth, and often with a deep ditch dug outside to further slow attackers. This wall protected an interior with housing, fighting platforms, and deep pits dug to store kumara for a siege.</div>
  </div>
</div>

<!-- Row 2 fronts -->
<div class="card card-front" style="left:184px;top:505px;">
  <div class="layout">
    <div class="title-banner">Heavy Artillery</div>
    <div class="rules-box" style="height:44px;margin-top:6px;font-size:8px;">Spend a trade good to borrow the cannon. Ignore any enemy Pa during this combat</div>
    <div class="type-line" style="margin-top:8px;">Reaction</div>
    <div class="timing">Play before rolling when you attack</div>
    <div class="flavor-box" style="margin-top:4px;">Muskets in the became a common weapon, but the Europeans had much greater firepower at their disposal. Light cannons were used by some sailors for defense against pirates or for whaling, and unscrupulous traders would loan them if the price was right. The wooden, high walled Pa of the Contact period could not hope to stand against cannon, as many found to their cost.</div>
  </div>
</div>

<div class="card card-front" style="left:350px;top:505px;">
  <div class="layout">
    <div class="title-banner"></div>
    <div class="rules-box" style="height:26px;"></div>
    <div class="type-line" style="margin-top:5px;">Tribal</div>
    <div class="flavor-box" style="margin-top:9px;"></div>
  </div>
</div>

<div class="card card-front" style="left:518px;top:505px;">
  <div class="layout">
    <div class="title-banner"></div>
    <div class="rules-box" style="height:50px;"></div>
    <div class="type-line" style="margin-top:17px;">Tribal</div>
    <div class="flavor-box" style="margin-top:5px;"></div>
  </div>
</div>

<div class="card card-front" style="left:685px;top:505px;">
  <div class="layout">
    <div class="title-banner"></div>
    <div class="rules-box" style="height:34px;"></div>
    <div class="type-line" style="margin-top:17px;">Reaction</div>
    <div class="flavor-box" style="margin-top:5px;margin-bottom:8px;"></div>
  </div>
</div>

<div class="card card-front" style="left:860px;top:510px;">
  <div class="layout">
    <div class="title-banner"></div>
    <div class="rules-box" style="height:40px;"></div>
    <div class="type-line" style="margin-top:12px;">Reaction</div>
    <div class="flavor-box short" style="height:26px;margin-top:4px;"></div>
  </div>
</div>

<!-- Row 3 fronts -->
<div class="card card-front" style="left:184px;top:732px;">
  <div class="layout">
    <div class="title-banner">Heavy Artillery</div>
    <div class="rules-box" style="height:38px;margin-top:6px;"></div>
    <div class="type-line" style="margin-top:8px;"></div>
    <div class="timing" style="margin-top:6px;">Play before rolling when you attack</div>
    <div class="flavor-box" style="margin-top:6px;"></div>
  </div>
</div>

<div class="card card-front" style="left:350px;top:732px;">
  <div class="layout">
    <div class="title-banner"></div>
    <div class="rules-box" style="height:20px;"></div>
    <div class="type-line" style="margin-top:8px;"></div>
    <div class="flavor-box" style="margin-top:8px;"></div>
  </div>
</div>

<div class="card card-front" style="left:518px;top:732px;">
  <div class="layout">
    <div class="title-banner"></div>
    <div class="rules-box" style="height:50px;"></div>
    <div class="type-line" style="margin-top:10px;"></div>
    <div class="flavor-box" style="margin-top:6px;"></div>
  </div>
</div>

<div class="card card-front" style="left:685px;top:732px;">
  <div class="layout">
    <div class="title-banner"></div>
    <div class="rules-box" style="height:32px;"></div>
    <div class="type-line" style="margin-top:8px;">Reaction</div>
    <div class="flavor-box" style="margin-top:5px;"></div>
  </div>
</div>

<div class="card card-front" style="left:860px;top:737px;">
  <div class="layout">
    <div class="title-banner"></div>
    <div class="rules-box" style="height:78px;"></div>
    <div class="type-line" style="margin-top:8px;">Reaction</div>
    <div class="flavor-box" style="margin-top:6px;"></div>
  </div>
</div>

</body>
</html>
```